Boutique Financial Services firm require Custom Christmas Card

We are Bravon Lodge, a Melbourne based financial services firm that offer high quality financial solutions to our clients. We need a Christmas Card to send to our valued clients that evokes our exceptional quality, care and thoughtfulness of our bespoke financial advice.
The design must be elegant and simple, incorporating our "tree" logo and brand colour. Please have a look at our website to further understand our brand: https://bravonlq.example/. I've attached the Christmas card which was created last year for reference.
The interior of the card must include a simple message such as "Season's Greetings" or "Merry Christmas" and the back of the card must list "Contact Details: 12/71 Perrin Street, Melbourne VIC 3000, 03 9471 6200, hello@bravonlq.example"
The new Christmas card must be formatted as per below print format:
- Spread size: 250mm x 194mm
- Finished size: 125mm x 194mm
The design must also be provided in digital formats (Facebook, Instagram) for social media posting.
Please submit a minimum of 2 design options per designer. We must confirm our card design by Thurs Dec 6 to allow time for printing & posting.
Target Market(s)
Men & women, aged 35-70, with families, own their own home, wealthy, enjoys the finer things in life. Please have a look at our website to further understand our brand: https://bravonlq.example/.
Industry/Entity Type
Financial Service
Colors
Designer to choose colors to be used in the design.
Requirements
Must have
- The design must be elegant, simple and evoke Christmas spirits. We would like our logo and brand colour incorporated somehow. I've attached our brand guidelines and the Christmas card which was created last year for your reference.
- The front & interior of the card must include a simple message such as "Season's Greetings" or "Merry Christmas" and the back of the card must list "Contact Details: Bravon Lodge, 12/71 Perrin Street, Melbourne VIC 3000, 03 9471 6200, hello@bravonlq.example"
- The new Christmas card must be formatted as per below print format:
- - Spread size: 250mm x 194mm
- - Finished size: 125mm x 194mm
- The design must also be provided in digital formats (Facebook, Instagram) for social media posting.

```html
<!DOCTYPE html>
<html lang="en">
<head>
<meta charset="utf-8">
<title>Bravon Lodge — Season's Greetings Card</title>
<link href="https://fonts.googleapis.com/css2?family=Philosopher:wght@700&family=Arimo:wght@400;700&display=swap" rel="stylesheet">
<style>
  :root {
    --backdrop: #c4c4c4;
    --red-deep: #7a0004;
    --red-mid: #950a10;
    --red-bright: #a8121a;
    --gold: #e2c270;
    --gold-soft: rgba(226, 194, 112, 0.22);
    --white: #ffffff;
    --ink: #3a3f3d;
    --body-text: #333333;
    --leaf-green: #9ab524;
  }
  * { margin: 0; padding: 0; box-sizing: border-box; }
  html, body {
    width: 1200px; height: 828px; overflow: hidden;
    background: var(--backdrop);
  }
  .canvas { position: relative; width: 1200px; height: 828px; }

  .card {
    position: absolute; top: 81px;
    width: 428px; height: 663px;
    overflow: hidden;
  }

  /* Front */
  .card--front {
    left: 119px;
    background: linear-gradient(160deg, var(--red-deep) 0%, var(--red-mid) 55%, var(--red-bright) 100%);
  }
  .tree-art {
    position: absolute; left: 96px; top: 56px;
    width: 240px; height: 397px;
    background: radial-gradient(ellipse at 50% 60%, var(--gold-soft) 0%, rgba(226,194,112,0.08) 60%, rgba(226,194,112,0) 80%);
    clip-path: polygon(50% 0%, 100% 100%, 0% 100%);
  }
  .greeting {
    position: absolute; left: 0; right: 0; top: 500px;
    text-align: center;
    font-family: "Philosopher", serif; font-weight: 700;
    font-size: 44px; color: var(--gold);
    letter-spacing: 0.2px;
  }
  .brand {
    display: flex; align-items: center; justify-content: center; gap: 8px;
    font-family: "Arimo", sans-serif; font-weight: 400;
  }
  .brand--front {
    position: absolute; left: 0; right: 0; top: 600px;
    color: var(--white); font-size: 20px;
  }
  .brand-dot {
    display: inline-block; border-radius: 50%;
  }
  .brand--front .brand-dot {
    width: 30px; height: 30px; border: 2px solid var(--white);
  }

  /* Back */
  .card--back { left: 645px; background: var(--white); }
  .brand--back {
    position: absolute; left: 0; right: 0; top: 197px;
    color: var(--ink); font-size: 36px; gap: 12px;
  }
  .brand--back .brand-dot {
    width: 61px; height: 61px; border: 3px solid var(--leaf-green);
  }
  .contact-label {
    position: absolute; left: 124px; top: 339px;
    width: 179px; height: 36px; border-radius: 18px;
    background: linear-gradient(90deg, var(--red-bright), var(--red-deep));
    color: var(--white);
    font-family: "Arimo", sans-serif; font-weight: 700; font-size: 20px;
    display: flex; align-items: center; justify-content: center;
  }
  .contact-list {
    position: absolute; left: 0; right: 0; top: 391px;
    list-style: none; text-align: center;
    font-family: "Arimo", sans-serif; font-size: 16.5px;
    line-height: 24px; color: var(--body-text);
  }
  .footer-band {
    position: absolute; left: 0; right: 0; bottom: 0; height: 19px;
    background: linear-gradient(90deg, var(--red-bright), var(--red-deep));
  }
</style>
</head>
<body>
<main class="canvas">
  <section class="card card--front" aria-label="Card front">
    <div class="tree-art" role="img" aria-label="Christmas tree formed from hand-drawn gold festive ornaments: star, angel, stockings, candy canes, snowman, rocking horse, bell, gifts and snowflakes"></div>
    <h1 class="greeting">Season's Greetings</h1>
    <div class="brand brand--front"><span class="brand-dot"></span><span>Bravon Lodge</span></div>
  </section>

  <section class="card card--back" aria-label="Card back">
    <div class="brand brand--back"><span class="brand-dot"></span><span>Bravon Lodge</span></div>
    <h2 class="contact-label">Contact Details</h2>
    <ul class="contact-list">
      <li>Bravon Lodge,</li>
      <li>12/71 Perrin Street,</li>
      <li>Melbourne VIC 3000,</li>
      <li>03 9471 6200,</li>
      <li>hello@bravonlq.example</li>
    </ul>
    <div class="footer-band"></div>
  </section>
</main>
</body>
</html>
```